BRIGHTWELL PROPERTY CHECKS Business card, please make it match the flyer.
Dana Kowalt
Dana@brightwellpropertychecksfl.example
352-555-0187 office
www.BrightwellPropertyChecks.example

Contact Information for Business Card

OUR LOGO

```html
<!DOCTYPE html>
<html lang="en">
<head>
<meta charset="utf-8">
<title>Brightwell Property Checks – Business Card</title>
<link rel="stylesheet" href="https://fonts.googleapis.com/css2?family=Montserrat:wght@800&family=Open+Sans:wght@400;600&display=swap">
<style>
  :root {
    --stage: #2b2b2b;
    --brand-red: #e3161c;
    --brand-blue: #0d3f78;
    --ink: #3a3a3a;
    --card-light-a: #ffffff;
    --card-light-b: #e3e6ea;
    --card-dark-a: #2a2022;
    --card-dark-b: #0f0b0c;
    --white: #ffffff;
  }
  html, body {
    margin: 0;
    padding: 0;
    width: 1200px;
    height: 866px;
    overflow: hidden;
    background: var(--stage);
  }
  .canvas {
    position: relative;
    width: 1200px;
    height: 866px;
  }
  .card {
    position: absolute;
    left: 320px;
    width: 560px;
    height: 320px;
    overflow: hidden;
    box-shadow: 0 10px 30px rgba(0,0,0,.55);
  }
  .card--front { top: 93px; }
  .card--back  { top: 453px; }

  .card__texture {
    position: absolute;
    inset: 0;
  }
  .card--front .card__texture {
    background: linear-gradient(155deg, var(--card-light-a) 0%, #f1f2f4 40%, var(--card-light-b) 100%);
  }
  .card--back .card__texture {
    background: radial-gradient(ellipse at 60% 45%, var(--card-dark-a) 0%, var(--card-dark-b) 75%);
  }

  .holder {
    position: absolute;
    left: 38px;
    top: 112px;
    font-family: "Open Sans", sans-serif;
    color: var(--ink);
  }
  .holder__name {
    margin: 0 0 10px;
    font-family: "Montserrat", sans-serif;
    font-weight: 800;
    font-size: 22px;
    letter-spacing: .5px;
    text-transform: uppercase;
    color: var(--brand-red);
  }
  .holder__line {
    display: flex;
    align-items: center;
    gap: 8px;
    margin: 0 0 4px;
    font-size: 13px;
  }
  .holder__line svg { flex: none; }

  .brand {
    position: absolute;
    display: flex;
    align-items: center;
    gap: 10px;
    font-family: "Montserrat", sans-serif;
    font-weight: 800;
    text-transform: uppercase;
    line-height: 1.1;
  }
  .card--front .brand {
    right: 34px;
    top: 110px;
    width: 220px;
    font-size: 19px;
    color: var(--brand-red);
  }
  .card--back .brand {
    left: 50%;
    top: 50%;
    transform: translate(-50%, -50%);
    width: 300px;
    font-size: 26px;
    color: var(--white);
  }
  .brand__dot {
    flex: none;
    border-radius: 50%;
    background: var(--brand-red);
  }
  .card--front .brand__dot { width: 22px; height: 22px; }
  .card--back .brand__dot  { width: 30px; height: 30px; }

  .website {
    position: absolute;
    right: 26px;
    bottom: 34px;
    margin: 0;
    font-family: "Open Sans", sans-serif;
    font-size: 13px;
    color: var(--ink);
  }
  .bands {
    position: absolute;
    left: 0;
    bottom: 0;
  }
</style>
</head>
<body>
<main class="canvas">

  <section class="card card--front" aria-label="Business card front">
    <div class="card__texture" role="img" aria-label="Light brushed metal surface with faint flag stars and diamond plate texture"></div>

    <div class="holder">
      <h1 class="holder__name">Dana Kowalt</h1>
      <p class="holder__line">
        <svg width="14" height="14" viewBox="0 0 24 24" aria-hidden="true"><path fill="#0d3f78" d="M6.6 10.8a15.1 15.1 0 0 0 6.6 6.6l2.2-2.2a1 1 0 0 1 1-.25 11.4 11.4 0 0 0 3.6.57 1 1 0 0 1 1 1V20a1 1 0 0 1-1 1A17 17 0 0 1 3 4a1 1 0 0 1 1-1h3.5a1 1 0 0 1 1 1c0 1.25.2 2.45.57 3.6a1 1 0 0 1-.25 1z"/></svg>
        352-555-0187
      </p>
      <p class="holder__line">
        <svg width="14" height="14" viewBox="0 0 24 24" aria-hidden="true"><path fill="#0d3f78" d="M2 5h20v14H2z"/><path fill="none" stroke="#fff" stroke-width="1.6" d="M2.5 5.5 12 13l9.5-7.5"/></svg>
        Dana@brightwellpropertychecksfl.example
      </p>
    </div>

    <div class="brand">
      <span class="brand__dot" aria-hidden="true"></span>
      <span class="brand__name">Brightwell Property Checks</span>
    </div>

    <p class="website">www.BrightwellPropertyChecks.example</p>

    <svg class="bands" width="560" height="26" viewBox="0 0 560 26" aria-hidden="true">
      <polygon points="0,0 300,0 290,26 0,26" fill="var(--brand-red)"/>
      <polygon points="300,0 306,0 296,26 290,26" fill="#ffffff"/>
      <polygon points="306,8 560,8 560,26 296,26" fill="var(--brand-blue)"/>
    </svg>
  </section>

  <section class="card card--back" aria-label="Business card back">
    <div class="card__texture" role="img" aria-label="Dark brushed metal surface with faint flag stars"></div>
    <div class="brand">
      <span class="brand__dot" aria-hidden="true"></span>
      <span class="brand__name">Brightwell Property Checks</span>
    </div>
  </section>

</main>
</body>
</html>
```